Business Card Design Project for Electrical Company

We need a business card designed for a new Electrical Company called Dorvel Electrical Solutions, i dont mind if only Dorvel Electrical is used. We are a domestic and commercial Electrical Company that provides a range of Electrical Services. Our Company colours are Fluro Yellow and Black with the Lightning bolt picture attached.I have attached a card that has been made i think it is rather basic and am looking for something more. the font of Dorvel Electrical has been used on our car graphics as well as the lightning bolt. i want to keep them the same so we can brand our business. Some things we want on the front of the card are Dorvel Electrical Solutions, Owen Platt, 0438516274, admin@dorvelelectrical.example, Lic No 58342, Servicing CQ Region. But we want Owens name seperate to the phone number as its the phone number for the office, owen wont be answering the phone so we are thinking we dont want to give that impression. What do you think? with all that if you have complete different font designs please submit what you think would work best. keeping in mind our company name and details as well as coulors.

Industry/Entity Type

Business

```html
<!DOCTYPE html>
<html lang="en">
<head>
<meta charset="utf-8">
<title>Dorvel Electrical Solutions – Business Card</title>
<link href="https://fonts.googleapis.com/css2?family=Open+Sans:ital,wght@0,400;0,600;0,700;0,800;1,700&display=swap" rel="stylesheet">
<style>
  :root {
    --fluro-yellow: #d6e32a;
    --olive-dark: #34360f;
    --olive-deep: #1d1e08;
    --black: #050505;
    --white: #ffffff;
    --ink: #111111;
    --silver-light: #f4f4f4;
    --silver-mid: #b9b9b9;
    --silver-dark: #6f6f6f;
    --bolt-glow: #cfe3ea;
    --page-bg: #e9e9e6;
  }
  * { box-sizing: border-box; margin: 0; padding: 0; }
  html, body {
    width: 1200px;
    height: 867px;
    overflow: hidden;
  }
  body {
    background: var(--page-bg);
    font-family: "Open Sans", Arial, sans-serif;
    position: relative;
  }

  .card {
    position: absolute;
    top: 270px;
    width: 540px;
    height: 327px;
    border-radius: 14px;
    overflow: hidden;
    box-shadow: 0 10px 28px rgba(0,0,0,0.22);
  }

  /* ---------- Back of card ---------- */
  .card--back {
    left: 40px;
    background: linear-gradient(120deg, var(--olive-dark) 0%, var(--olive-deep) 45%, var(--black) 75%);
  }
  .card--back .bolt-art {
    position: absolute;
    top: 0;
    right: 0;
    width: 250px;
    height: 190px;
    background: radial-gradient(ellipse at 70% 30%, rgba(220,225,230,0.55) 0%, rgba(160,165,170,0.18) 45%, rgba(0,0,0,0) 75%);
  }
  .card--back .brand-name {
    position: absolute;
    left: 120px;
    top: 92px;
    color: var(--fluro-yellow);
    font-weight: 800;
    font-size: 44px;
    line-height: 44px;
    text-transform: uppercase;
    letter-spacing: 0.5px;
  }
  .card--back .brand-name span { display: block; }
  .card--back .brand-name .brand-sub {
    font-size: 24px;
    line-height: 30px;
    padding-left: 150px;
    letter-spacing: 1px;
  }
  .card--back .tagline-band {
    position: absolute;
    left: 0;
    right: 0;
    top: 232px;
    height: 44px;
    background: linear-gradient(90deg, var(--silver-dark) 0%, var(--silver-light) 25%, var(--silver-mid) 55%, var(--silver-light) 80%, var(--silver-dark) 100%);
    display: flex;
    align-items: center;
    padding-left: 150px;
  }
  .card--back .tagline {
    font-style: italic;
    font-weight: 700;
    font-size: 22px;
    letter-spacing: 1.5px;
    color: var(--ink);
  }

  /* ---------- Front of card ---------- */
  .card--front {
    left: 620px;
    background: var(--white);
  }
  .card--front .bolt-art--faint {
    position: absolute;
    left: 0;
    top: 30px;
    width: 110px;
    height: 150px;
    background: radial-gradient(ellipse at 60% 40%, rgba(120,120,120,0.25) 0%, rgba(255,255,255,0) 70%);
  }
  .card--front .brand-name {
    position: absolute;
    left: 44px;
    top: 34px;
    color: var(--olive-dark);
    font-weight: 800;
    font-size: 36px;
    line-height: 36px;
    text-transform: uppercase;
    letter-spacing: 0.5px;
  }
  .card--front .brand-name span { display: block; }
  .card--front .brand-name .brand-sub {
    font-size: 20px;
    line-height: 26px;
    padding-left: 120px;
    letter-spacing: 1px;
  }
  .card--front .person-name {
    position: absolute;
    right: 40px;
    top: 110px;
    font-weight: 600;
    font-size: 30px;
    color: var(--ink);
  }
  .card--front .contact {
    position: absolute;
    left: 58px;
    top: 160px;
    font-weight: 700;
    font-size: 17px;
    line-height: 25px;
    color: var(--ink);
    list-style: none;
  }
  .card--front .licence {
    position: absolute;
    left: 40px;
    top: 222px;
    font-size: 15px;
    color: var(--ink);
  }
  .card--front .silver-rule {
    position: absolute;
    left: 0;
    right: 0;
    top: 250px;
    height: 6px;
    background: linear-gradient(90deg, var(--silver-dark), var(--silver-light) 40%, var(--silver-mid) 70%, var(--silver-dark));
  }
  .card--front .region-band {
    position: absolute;
    left: 0;
    right: 0;
    top: 256px;
    bottom: 0;
    background: linear-gradient(100deg, var(--olive-dark) 0%, var(--olive-deep) 50%, var(--black) 100%);
    display: flex;
    align-items: center;
    padding-left: 40px;
  }
  .card--front .region {
    font-style: italic;
    font-weight: 700;
    font-size: 22px;
    color: var(--fluro-yellow);
  }
  .card--front .bolt-art--corner {
    position: absolute;
    right: 0;
    bottom: 0;
    width: 150px;
    height: 71px;
    background: radial-gradient(ellipse at 60% 50%, rgba(207,227,234,0.55) 0%, rgba(0,0,0,0) 70%);
  }
</style>
</head>
<body>

  <section class="card card--back" aria-label="Business card back">
    <div class="bolt-art" role="img" aria-label="Lightning bolt artwork"></div>
    <h1 class="brand-name">
      <span>Dorvel</span>
      <span>Electrical</span>
      <span class="brand-sub">Solutions</span>
    </h1>
    <div class="tagline-band">
      <p class="tagline">Lightning Up CQ!</p>
    </div>
  </section>

  <section class="card card--front" aria-label="Business card front">
    <div class="bolt-art--faint" role="img" aria-label="Faint lightning bolt artwork"></div>
    <h2 class="brand-name">
      <span>Dorvel</span>
      <span>Electrical</span>
      <span class="brand-sub">Solutions</span>
    </h2>
    <p class="person-name">Owen Platt</p>
    <ul class="contact">
      <li class="phone">0438516274</li>
      <li class="email">admin@dorvelelectrical.example</li>
    </ul>
    <p class="licence">Lic No. 58342</p>
    <div class="silver-rule"></div>
    <div class="region-band">
      <p class="region">Servicing CQ Region</p>
    </div>
    <div class="bolt-art--corner" role="img" aria-label="Lightning bolt artwork"></div>
  </section>

</body>
</html>
```